Book cover for "Steady Harbor" focused on scaling up an Insurance Agency

Front Cover:
We need book cover for our upcoming book with title "Steady Harbor" . Subtitle of book is "The secrets behind building a multi-million dollar Insurance agency:Interviews, success stories and framework for success".
On top line it should say " Foreword by Mark Vellison".
Author name : "Rajendra Kulkat"
This book will help insurance agents in scaling up their agency. It will also help someone looking to start a business or side hustle.

Back Cover:
It should contain content provided below and image of author attached.
"
Who should read this book?

Do you know that starting an Insurance Agency is probably one of the best business ideas?
Do you want to know how some startups created billion dollar plus insurance based companies in the last 5-10 years?
Do you want to know the secrets behind building a multi-million dollar Insurance agency?
Do you want to know how to scale up an Insurance Agency profitably?
Do you want to know how to cut through the noise in the market and differentiate your business?
How to leverage technology to rise above (be seen and heard) the myriad of agencies around you and compete with both local and online agencies?
How to build a team which carries your mindset to take care of clients and grow your business?
(above list should be bulleted)
If you are interested in learning about these topics then you are at the right place.

You can either spend years figuring out things yourself or read this book and get wisdom from successful agents and thought leaders at top insurance agencies."

Spine:
" Steady Harbor by Rajendra Kulkat"

Requirements:
One file should be only book cover.
Other file should contain :front cover, back cover and spine as one file.
It should follow standard for Brimlow Press, link provided below.
https://print.brimlowpress.example/en_US/help/topic/Q738210465

Target Market(s)

Insurance Agents
People looking to start a new business
Side Hustlers

Industry/Entity Type

Insurance Agency

Font styles to use
Serif

```html
<!DOCTYPE html>
<html lang="en">
<head>
<meta charset="utf-8">
<title>Steady Harbor – Full Cover Wrap</title>
<link rel="stylesheet" href="https://fonts.googleapis.com/css2?family=Cinzel:wght@400;500;600&family=Crimson+Text:ital@1&family=Lato:wght@400;700&family=Arvo:wght@700&display=swap">
<style>
  :root {
    --navy: #0a2a6c;
    --title-navy: #0e2b72;
    --maroon: #6e1222;
    --body-ink: #1c2b5e;
    --sage: #b7c693;
    --cream: #f7f9ee;
    --white: #ffffff;
    --photo-blue: #8fb3dc;
    --photo-suit: #b9c0c8;
  }
  * { margin: 0; padding: 0; box-sizing: border-box; }
  html, body { width: 1200px; height: 842px; overflow: hidden; background: var(--white); }

  .cover-wrap { position: relative; width: 1200px; height: 842px; overflow: hidden; }

  .panel { position: absolute; top: 0; height: 842px; }
  .back-cover {
    left: 0; width: 562px; z-index: 0;
    background: radial-gradient(ellipse at 60% 45%, var(--cream) 0%, #eef2dc 45%, var(--sage) 110%);
  }
  .front-cover {
    left: 638px; width: 562px; z-index: 0;
    background: radial-gradient(ellipse at 45% 55%, var(--cream) 0%, #eef2dc 45%, var(--sage) 110%);
  }
  .base-band { position: absolute; left: 0; right: 0; top: 736px; bottom: 0; background: var(--navy); z-index: 1; }
  .spine { left: 562px; width: 76px; background: var(--navy); z-index: 2; }

  /* Back cover */
  .back-title {
    position: absolute; top: 32px; left: 0; width: 562px; text-align: center;
    font-family: "Cinzel", serif; font-weight: 600; font-size: 39px; color: var(--maroon);
    letter-spacing: 1px;
  }
  .back-copy {
    position: absolute; top: 106px; left: 54px; width: 448px;
    font-family: "Lato", sans-serif; font-size: 14.6px; line-height: 18.8px; color: var(--body-ink);
  }
  .back-copy .gap { margin-top: 18.8px; }

  .author-photo {
    position: absolute; left: 54px; top: 588px; width: 206px; height: 254px; z-index: 3;
    background: linear-gradient(180deg, #d9dde2 0%, var(--photo-suit) 60%, #9aa3ad 100%);
  }
  .barcode-box { position: absolute; left: 353px; top: 696px; width: 170px; height: 101px; background: var(--white); z-index: 3; }

  /* Spine */
  .spine-text {
    position: absolute; left: 0; width: 76px; writing-mode: vertical-rl;
    display: flex; align-items: center; justify-content: flex-start;
    color: var(--white); white-space: nowrap;
  }
  .spine-title { top: 36px; height: 400px; font-family: "Cinzel", serif; font-size: 41px; letter-spacing: 1px; }
  .spine-author { top: 500px; height: 320px; font-family: "Arvo", serif; font-weight: 700; font-size: 27px; }

  /* Front cover */
  .foreword {
    position: absolute; top: 36px; left: 0; width: 562px; text-align: center;
    font-family: "Lato", sans-serif; font-weight: 700; font-size: 16px; color: var(--maroon);
  }
  .front-title {
    position: absolute; top: 80px; left: 0; width: 562px; text-align: center;
    font-family: "Cinzel", serif; font-weight: 500; font-size: 92px; line-height: 96px;
    color: var(--title-navy);
  }
  .subtitle {
    position: absolute; top: 286px; left: 0; width: 562px; text-align: center;
    font-family: "Crimson Text", serif; font-style: italic; font-size: 24px; line-height: 24px;
    color: var(--maroon);
  }
  .hero-art {
    position: absolute; left: 94px; top: 376px; width: 404px; height: 352px;
    background: radial-gradient(ellipse at 40% 40%, var(--photo-blue) 0%, #c7d6b8 55%, rgba(238,242,220,0) 75%);
  }
  .front-author {
    position: absolute; top: 765px; left: 638px; width: 562px; text-align: center; z-index: 3;
    font-family: "Arvo", serif; font-weight: 700; font-size: 37px; color: var(--white);
    letter-spacing: 1px;
  }
</style>
</head>
<body>
<main class="cover-wrap">
  <section class="panel back-cover">
    <h2 class="back-title">STEADY HARBOR</h2>
    <div class="back-copy">
      <p>Who should read this book?</p>
      <p class="gap">Do you know that starting an Insurance Agency is probably one of the best business ideas?</p>
      <p>Do you want to know how some startups created billion dollar plus insurance based companies in the last 5-10 years?</p>
      <p>Do you want to know the secrets behind building a multi-million dollar Insurance agency?</p>
      <p>Do you want to know how to scale up an Insurance Agency profitably?</p>
      <p>Do you want to know how to cut through the noise in the market and differentiate your business?</p>
      <p>How to leverage technology to rise above (be seen and heard) the myriad of agencies around you and compete with both local and online agencies?</p>
      <p>How to build a team which carries your mindset to take care of clients and grow your business?</p>
      <p>(above list should be bulleted)</p>
      <p>If you are interested in learning about these topics then you are at the right place.</p>
      <p class="gap">You can either spend years figuring out things yourself or read this book and get wisdom from successful agents and thought leaders at top insurance agencies.</p>
    </div>
  </section>

  <section class="panel front-cover">
    <p class="foreword">FOREWORD BY MARK VELLISON</p>
    <h1 class="front-title">STEADY<br>HARBOR</h1>
    <p class="subtitle">The secrets behind building a<br>multi-million dollar Insurance agency :<br>Interviews, success stories and framework for success</p>
    <div class="hero-art" role="img" aria-label="Photo of a smiling businessman in a blue shirt carrying a briefcase, climbing steps made of hundred-dollar bills"></div>
  </section>

  <div class="base-band"></div>

  <section class="panel spine">
    <div class="spine-text spine-title">STEADY HARBOR</div>
    <div class="spine-text spine-author">RAJENDRA KULKAT</div>
  </section>

  <div class="author-photo" role="img" aria-label="Portrait photo of the author in a light grey blazer"></div>
  <div class="barcode-box"></div>
  <div class="front-author">RAJENDRA KULKAT</div>
</main>
</body>
</html>
```